Coral Marriage Counsel Partners Billboard

We are looking for a billboard design for a Florida divorce law firm. We are unique in the legal field for offering flat fee pricing. Other law firms are expensive, charging hourly rates. We have A LOT of lawyers advertising for personal injury, so we are looking for something fun that will catch the attention and drive home the message that we are an affordable firm to hire for their divorce because we charge a fixed fee. We want people to be directed to steadyratesplit.example

Target Market(s)

Individual seeking a fast and affordable divorce at a fixed fee instead of hourly

Industry/Entity Type

Legal

Requirements
Must have
• Name of firm, logo, steadyratesplit.example, and in small font: Main Office Marisol Bay
Should not have
• Promises. Price

```html
<!DOCTYPE html>
<html lang="en">
<head>
<meta charset="utf-8">
<title>Coral Marriage Counsel Partners Billboard</title>
<link href="https://fonts.googleapis.com/css2?family=Montserrat:wght@400;500;600;700;800&display=swap" rel="stylesheet">
<style>
  :root {
    --navy: #1f4670;
    --gold: #a77d1e;
    --white: #ffffff;
    --ground: #e4e4e6;
    --photo-dark: #596274;
    --photo-light: #a4a9b4;
  }
  * { margin: 0; padding: 0; box-sizing: border-box; }
  html, body { width: 1121px; height: 1200px; overflow: hidden; }
  body {
    background: var(--ground);
    font-family: "Montserrat", sans-serif;
    position: relative;
  }
  .billboard {
    position: absolute;
    left: 40px; top: 427px;
    width: 1040px; height: 346px;
    background: var(--white);
    overflow: hidden;
    box-shadow: 6px 8px 14px rgba(0,0,0,0.25);
  }
  .portrait-band {
    position: absolute; left: 0; top: 0;
    width: 560px; height: 346px;
  }
  .name-plate {
    position: absolute; left: 0; top: 282px;
    width: 232px; height: 54px;
    background: var(--gold);
    clip-path: polygon(0 0, 100% 0, 94% 100%, 0 100%);
    color: var(--white);
    text-align: center;
    padding-top: 8px;
  }
  .name-plate .attorney-name { font-weight: 700; font-size: 17px; line-height: 20px; }
  .name-plate .attorney-role { font-weight: 400; font-size: 14px; line-height: 18px; }
  .brand {
    position: absolute; left: 584px; width: 400px; top: 19px;
    text-align: center;
  }
  .brand-dot {
    width: 42px; height: 42px; border-radius: 50%;
    background: var(--navy);
    border: 3px solid var(--gold);
    margin: 0 auto 10px;
  }
  .brand-name {
    font-weight: 600; font-size: 13px; letter-spacing: 1px;
    color: var(--navy); text-transform: uppercase;
  }
  .headline {
    position: absolute; left: 560px; width: 448px; top: 103px;
    text-align: center; font-weight: 800; font-size: 33px; line-height: 40px;
  }
  .headline .line-gold { color: var(--gold); display: block; }
  .headline .line-navy { color: var(--navy); display: block; }
  .features {
    position: absolute; left: 596px; top: 215px;
    width: 374px; height: 67px;
    background: var(--navy);
    display: flex;
  }
  .feature {
    flex: 1; position: relative;
    color: var(--white); font-weight: 700; font-size: 10.5px; line-height: 14px;
    text-align: center; padding-top: 28px;
  }
  .feature + .feature::before {
    content: ""; position: absolute; left: 0; top: 9px; bottom: 9px;
    width: 1px; background: rgba(255,255,255,0.7);
  }
  .feature-icon {
    position: absolute; left: 50%; top: -20px;
    width: 36px; height: 36px; margin-left: -18px;
  }
  .contact {
    position: absolute; left: 560px; width: 448px; top: 293px;
    text-align: center; font-size: 17px; color: var(--navy); font-weight: 500;
  }
  .contact .call { color: var(--gold); font-weight: 700; }
  .contact .phone { color: var(--navy); font-weight: 700; }
  .contact .divider { color: var(--navy); font-weight: 400; margin: 0 4px; }
  .contact .site-key { color: var(--gold); font-weight: 600; }
  .office {
    position: absolute; left: 596px; width: 374px; top: 319px;
    display: flex; align-items: center; gap: 8px;
    font-size: 13px; font-weight: 800; color: var(--navy);
  }
  .office .rule { flex: 1; height: 1px; background: var(--navy); }
  .office .label { font-size: 9px; font-weight: 600; color: var(--gold); margin-right: 3px; }
</style>
</head>
<body>
  <div class="billboard">
    <svg class="portrait-band" viewBox="0 0 560 346" preserveAspectRatio="none">
      <defs>
        <linearGradient id="photoTone" x1="0" y1="0" x2="1" y2="1">
          <stop offset="0" stop-color="var(--photo-dark)"/>
          <stop offset="1" stop-color="var(--photo-light)"/>
        </linearGradient>
      </defs>
      <path d="M0,0 H462 C557,80 557,260 470,346 H0 Z" fill="var(--gold)"/>
      <path d="M0,0 H458 C541,80 541,260 462,346 H0 Z" fill="var(--white)"/>
      <path d="M0,0 H455 C528,80 528,260 455,346 H0 Z" fill="var(--navy)"/>
      <path d="M0,0 H396 C484,80 484,265 404,346 H0 Z" fill="var(--white)"/>
      <path d="M0,0 H392 C480,80 480,265 400,346 H0 Z" fill="url(#photoTone)" role="img" aria-label="Portrait photo of the attorney in a dark suit and tie"/>
    </svg>
    <div class="name-plate">
      <div class="attorney-name">Marco D. Alvarez</div>
      <div class="attorney-role">Divorce Attorneys</div>
    </div>

    <div class="brand">
      <div class="brand-dot"></div>
      <div class="brand-name">Coral Marriage Counsel Partners</div>
    </div>

    <h1 class="headline">
      <span class="line-gold">Are You In Need Of</span>
      <span class="line-navy">A Divorce Attorney?</span>
    </h1>

    <div class="features">
      <div class="feature">
        <svg class="feature-icon" viewBox="0 0 36 36">
          <circle cx="18" cy="18" r="17" fill="var(--gold)" stroke="var(--white)" stroke-width="1.5"/>
          <circle cx="18" cy="18" r="9" fill="none" stroke="var(--white)" stroke-width="1.6"/>
          <path d="M18 12 V18 H22" fill="none" stroke="var(--white)" stroke-width="1.6"/>
        </svg>
        24/7<br>Availability
      </div>
      <div class="feature">
        <svg class="feature-icon" viewBox="0 0 36 36">
          <circle cx="18" cy="18" r="17" fill="var(--gold)" stroke="var(--white)" stroke-width="1.5"/>
          <path d="M18 9 V26 M13 26 H23 M10 13 H26 M10 13 L7.5 19 H12.5 Z M26 13 L23.5 19 H28.5 Z" fill="none" stroke="var(--white)" stroke-width="1.4"/>
        </svg>
        Flat Fee<br>for most cases
      </div>
      <div class="feature">
        <svg class="feature-icon" viewBox="0 0 36 36">
          <circle cx="18" cy="18" r="17" fill="var(--gold)" stroke="var(--white)" stroke-width="1.5"/>
          <path d="M8 17 L13 12 L18 15 L23 12 L28 17 L20 25 Q18 27 16 25 Z M13 19 L17 23 M15 17 L19 21" fill="none" stroke="var(--white)" stroke-width="1.4" stroke-linejoin="round"/>
        </svg>
        100%<br>Dedicated
      </div>
      <div class="feature">
        <svg class="feature-icon" viewBox="0 0 36 36">
          <circle cx="18" cy="18" r="17" fill="var(--gold)" stroke="var(--white)" stroke-width="1.5"/>
          <rect x="10" y="11" width="16" height="15" fill="none" stroke="var(--white)" stroke-width="1.4"/>
          <path d="M10 15 H26 M14 9 V13 M22 9 V13 M13 18 H15 M17 18 H19 M21 18 H23 M13 22 H15 M17 22 H19 M21 22 H23" stroke="var(--white)" stroke-width="1.3"/>
        </svg>
        20 Years<br>in Practice
      </div>
    </div>

    <div class="contact">
      <span class="call">Call</span> <span class="phone">555-014-2277</span><span class="divider">|</span>www.<span class="site-key">steadyrate</span>split.example
    </div>

    <div class="office">
      <span class="rule"></span>
      <span><span class="label">Main Office</span>Marisol Bay</span>
      <span class="rule"></span>
    </div>
  </div>
</body>
</html>
```